Refresh of The Marston Collective business card

Update business card design using existing primary logo. Names, numbers, etc. are too hard to read on current design.

Target Market(s)

We are a CPA firm.

Industry/Entity Type

Accountant

Contact Information for Business Card

update current card

Colors
0355a3
3176b5
85acd3
0792cd

Requirements
Must have
• Easier to read phone numbers and names
• Use existing logo
Nice to have
• We love our color scheme and current TMC logo. But the names and phone numbers are too small and card just look old and stale.

```html
<!DOCTYPE html>
<html lang="en">
<head>
<meta charset="utf-8">
<title>The Marston Collective — Business Card</title>
<link rel="stylesheet" href="https://fonts.googleapis.com/css2?family=Cinzel:wght@400;600&family=Mulish:wght@400&display=swap">
<style>
  :root {
    --backdrop: #e4e4e4;
    --navy-deep: #062560;
    --blue-primary: #0355a3;
    --blue-mid: #3176b5;
    --blue-light: #85acd3;
    --paper: #f7f7f7;
    --steel: #3c3c3c;
    --white: #ffffff;
  }
  * { margin: 0; padding: 0; box-sizing: border-box; }
  html, body {
    width: 1200px; height: 576px; overflow: hidden;
    background: var(--backdrop);
  }
  .stage { position: relative; width: 1200px; height: 576px; }

  .card {
    position: absolute; top: 138px;
    width: 484px; height: 294px;
    border-radius: 12px; overflow: hidden;
    box-shadow: 0 2px 6px rgba(0,0,0,0.25);
  }

  /* Front */
  .card--front {
    left: 82px;
    background: radial-gradient(ellipse 70% 75% at 45% 40%, #0b5cb6 0%, var(--blue-primary) 40%, var(--navy-deep) 100%);
    color: var(--white);
  }
  .front-mark {
    position: absolute; left: 104px; top: 86px;
    width: 92px; height: 92px; border-radius: 50%;
    border: 3px solid var(--white);
  }
  .front-name {
    position: absolute; left: 212px; top: 100px;
    font-family: "Cinzel", serif; font-weight: 600;
    font-size: 26px; line-height: 30px; letter-spacing: 0.5px;
    color: var(--white);
  }
  .front-web {
    position: absolute; left: 0; right: 0; top: 254px;
    text-align: center;
    font-family: "Mulish", sans-serif; font-size: 13.5px;
    color: #dfe8f5; letter-spacing: 0.3px;
  }

  /* Back */
  .card--back { left: 602px; background: var(--paper); }
  .back-shape { position: absolute; inset: 0; }
  .back-text {
    position: absolute; left: 24px; color: var(--white);
    font-family: "Mulish", sans-serif;
  }
  .person-name {
    top: 32px;
    font-family: "Cinzel", serif; font-weight: 400;
    font-size: 19px; letter-spacing: 0.3px;
  }
  .person-title { top: 56px; font-size: 13px; }
  .address { top: 164px; font-size: 13px; line-height: 17px; }
  .contact-list {
    top: 206px; list-style: none;
    font-size: 13px; line-height: 17px;
  }
  .contact-list li { display: flex; align-items: center; gap: 8px; }
  .contact-list svg { width: 11px; height: 11px; fill: var(--white); flex: none; }

  .back-logo-name {
    position: absolute; left: 386px; top: 20px;
    width: 62px; height: 160px;
    writing-mode: vertical-rl; transform: rotate(180deg);
    font-family: "Cinzel", serif; font-weight: 600;
    font-size: 21px; line-height: 27px;
    color: var(--blue-primary); text-align: center;
  }
  .back-mark {
    position: absolute; left: 354px; top: 186px;
    width: 76px; height: 76px; border-radius: 50%;
    background: radial-gradient(circle at 40% 35%, var(--blue-mid), var(--blue-primary) 60%, var(--navy-deep));
  }
</style>
</head>
<body>
<main class="stage">

  <section class="card card--front" aria-label="Card front">
    <div class="front-mark"></div>
    <p class="front-name">The Marston<br>Collective</p>
    <p class="front-web">www.marstoncollective.com</p>
  </section>

  <section class="card card--back" aria-label="Card back">
    <svg class="back-shape" viewBox="0 0 484 294" preserveAspectRatio="none" aria-hidden="true">
      <defs>
        <radialGradient id="backBlue" cx="0.35" cy="0.5" r="0.75">
          <stop offset="0" stop-color="#0b5cb6"/>
          <stop offset="0.45" stop-color="#0355a3"/>
          <stop offset="1" stop-color="#062560"/>
        </radialGradient>
      </defs>
      <path d="M0 0 H340 Q270 40 275 150 Q280 240 340 294 H0 Z" fill="var(--steel)"/>
      <path d="M0 0 H316 Q258 50 262 150 Q268 240 318 294 H0 Z" fill="url(#backBlue)"/>
    </svg>

    <h1 class="back-text person-name">Daniel R. Marston, CPA</h1>
    <p class="back-text person-title">President</p>
    <p class="back-text address">312 E. Alden Ave. Suite 104<br>Winter Park, Florida 32789</p>
    <ul class="back-text contact-list">
      <li><svg viewBox="0 0 12 12"><path d="M1 4 Q6 0 11 4 L10 6 L8 5 L8 4 Q6 3 4 4 L4 5 L2 6 Z M3 7 H9 L10 11 H2 Z"/></svg>407.555.0142</li>
      <li><svg viewBox="0 0 12 12"><path d="M3 1 H9 V4 H3 Z M1 5 H11 V9 H9 V7 H3 V9 H1 Z M3 8 H9 V11 H3 Z"/></svg>407.555.0187</li>
      <li><svg viewBox="0 0 12 12"><path d="M3 0 H9 V12 H3 Z M4 2 V9 H8 V2 Z"/></svg>407.555.0163</li>
      <li><svg viewBox="0 0 12 12"><path d="M0 2 H12 L6 7 Z M0 3.5 L6 8.5 L12 3.5 V10 H0 Z"/></svg>dan@marstoncollective.com</li>
    </ul>

    <p class="back-logo-name">The Marston<br>Collective</p>
    <div class="back-mark"></div>
  </section>

</main>
</body>
</html>
```